New Stationery New Logo for KT Mouldings Limited

We have a new logo and now want new stationary to go with it

This will be

Letterhead
Compliments Slip
Business Cards

Company details are
KT Mouldings Limited
Brindle Row, Rugby, Warwickshire, CV34 7HX, UK
Telephone : +44(0)1788 930467
Fax: +44(0)1788 918723
Email: sales@ktmouldings.example
Web: www.ktmouldings.example

Target Market(s)

Engineering / Metal Stamping

Industry/Entity Type

Manufacture

Contact Information for Business Card

Neil Garbutt
Business Development Manager
KT Mouldings Limited
Brindle Row
Rugby
Warwickshire
CV34 7HX, UK

T: +44(0)1788 930467
F: +44(0)1788 918723
E: sales@ktmouldings.example
W: www.ktmouldings.example

Font styles to use
Sans Serif

Colors
33a6d7
0555a3
3176b5
85cae6
85acd3

Requirements
Must have
• Logo

```html
<!DOCTYPE html>
<html lang="en">
<head>
<meta charset="utf-8">
<title>KT Mouldings Limited – Business Cards</title>
<link href="https://fonts.googleapis.com/css2?family=Open+Sans:wght@400;600&family=Roboto+Condensed:wght@400;700&display=swap" rel="stylesheet">
<style>
  :root {
    --navy: #0f2f6e;
    --blue-deep: #1f4f9c;
    --blue-mid: #3176b5;
    --blue-light: #85acd3;
    --grey-text: #7a7f88;
    --rule: #b8bcc4;
    --paper: #ffffff;
    --backdrop: #e9ebef;
  }
  * { box-sizing: border-box; margin: 0; padding: 0; }
  html, body { width: 1200px; height: 800px; overflow: hidden; }
  body {
    background: var(--backdrop);
    font-family: "Open Sans", Arial, sans-serif;
    position: relative;
  }
  .card {
    position: absolute;
    width: 520px;
    height: 300px;
    top: 250px;
    box-shadow: 0 6px 18px rgba(0,0,0,0.18);
    overflow: hidden;
  }
  .card--front { left: 620px; display: flex; background: var(--paper); }
  .card--back {
    left: 60px;
    background: radial-gradient(ellipse at 50% 40%, var(--blue-mid) 0%, var(--blue-deep) 55%, #163f86 100%);
    display: flex; flex-direction: column; align-items: center; justify-content: center;
  }
  .front__brand {
    width: 57%;
    display: flex; flex-direction: column; align-items: center; justify-content: center;
  }
  .brand-name {
    display: flex; align-items: center; gap: 10px;
    font-family: "Open Sans", Arial, sans-serif;
    font-weight: 600;
    letter-spacing: 0.28em;
    color: var(--navy);
    font-size: 19px;
  }
  .brand-mark { width: 12px; height: 12px; background: var(--navy); }
  .brand-rule { width: 200px; height: 1px; background: var(--rule); margin: 12px 0 8px; }
  .brand-legal {
    font-family: "Roboto Condensed", Arial, sans-serif;
    font-size: 17px; color: var(--grey-text);
  }
  .front__contact {
    width: 43%;
    background: linear-gradient(160deg, var(--blue-deep) 0%, var(--blue-mid) 100%);
    color: var(--paper);
    padding: 66px 18px 0 22px;
  }
  .contact-name {
    font-family: "Roboto Condensed", Arial, sans-serif;
    font-weight: 700; font-size: 17px; margin-bottom: 8px;
  }
  .contact-list { list-style: none; font-size: 9.5px; line-height: 1.55; }
  .contact-list li { display: flex; gap: 7px; align-items: flex-start; }
  .contact-list svg { flex: none; width: 10px; height: 10px; margin-top: 2px; }
  .card--back .brand-name { color: var(--navy); font-size: 30px; gap: 14px; }
  .card--back .brand-mark { width: 18px; height: 18px; background: var(--navy); }
  .back__web {
    margin-top: 22px;
    font-family: "Roboto Condensed", Arial, sans-serif;
    font-weight: 700; font-size: 22px; color: var(--paper);
  }
</style>
</head>
<body>
  <section class="card card--back" aria-label="Business card, back">
    <div class="brand-name"><span class="brand-mark"></span>KT MOULDINGS</div>
    <p class="back__web">www.ktmouldings.example</p>
  </section>

  <section class="card card--front" aria-label="Business card, front">
    <div class="front__brand">
      <div class="brand-name"><span class="brand-mark"></span>KT MOULDINGS</div>
      <div class="brand-rule"></div>
      <p class="brand-legal">KT Mouldings Limited</p>
    </div>
    <div class="front__contact">
      <p class="contact-name">Example Name</p>
      <ul class="contact-list">
        <li>
          <svg viewBox="0 0 10 10"><circle cx="5" cy="5" r="5" fill="#fff"/><path d="M5 2.2a1.8 1.8 0 0 1 1.8 1.8C6.8 5.4 5 7.8 5 7.8S3.2 5.4 3.2 4A1.8 1.8 0 0 1 5 2.2z" fill="#1f4f9c"/></svg>
          <span>Brindle Row, Rugby, Warwickshire,<br>CV34 7HX, UK</span>
        </li>
        <li>
          <svg viewBox="0 0 10 10"><circle cx="5" cy="5" r="5" fill="#fff"/><path d="M3.4 2.6l1 1-.6.7a3.4 3.4 0 0 0 1.9 1.9l.7-.6 1 1-.7.8C4.8 7.2 2.8 5.2 2.6 3.3z" fill="#1f4f9c"/></svg>
          <span>+44(0)1788 930467</span>
        </li>
        <li>
          <svg viewBox="0 0 10 10"><circle cx="5" cy="5" r="5" fill="#fff"/><rect x="2.6" y="4" width="4.8" height="3" fill="#1f4f9c"/><rect x="3.4" y="2.6" width="3.2" height="1.6" fill="#1f4f9c"/></svg>
          <span>+44(0)1788 918723</span>
        </li>
        <li>
          <svg viewBox="0 0 10 10"><circle cx="5" cy="5" r="5" fill="#fff"/><rect x="2.4" y="3.2" width="5.2" height="3.6" fill="#1f4f9c"/><path d="M2.4 3.2L5 5.2l2.6-2" stroke="#fff" stroke-width=".6" fill="none"/></svg>
          <span>sales@ktmouldings.example</span>
        </li>
        <li>
          <svg viewBox="0 0 10 10"><circle cx="5" cy="5" r="5" fill="#fff"/><circle cx="5" cy="5" r="2.6" fill="none" stroke="#1f4f9c" stroke-width=".7"/><path d="M2.4 5h5.2M5 2.4c-1.4 1.6-1.4 3.6 0 5.2M5 2.4c1.4 1.6 1.4 3.6 0 5.2" stroke="#1f4f9c" stroke-width=".5" fill="none"/></svg>
          <span>www.ktmouldings.example</span>
        </li>
      </ul>
    </div>
  </section>
</body>
</html>
```